Power point Presentation Template 2

I am looking a professionally designed Powerpoint Presentation template for my company. We are Information Technology Company. I have attached the Logo. The Logo will also give an indication of which colours to be used in the design.

Information and Communication Technology

• All ideas welcomed
• Professional Look and Feel

```html
<!DOCTYPE html>
<html lang="en">
<head>
<meta charset="utf-8">
<title>Velantis Technologies – Presentation Template</title>
<link rel="stylesheet" href="https://fonts.googleapis.com/css2?family=Montserrat:wght@400;600;700&family=Open+Sans:wght@400;600&display=swap">
<style>
:root{
  --orange:#f7901e;
  --orange-deep:#e77f0e;
  --orange-soft:#f9ab55;
  --ink:#2b2b2b;
  --text:#4d4d4d;
  --bar:#262626;
  --navy:#143a62;
  --grey:#9b9b9b;
  --grey-light:#d4d4d4;
  --white:#ffffff;
}
*{box-sizing:border-box;margin:0;padding:0}
html,body{width:1200px;height:1155px;overflow:hidden}
body{background:var(--navy);font-family:"Open Sans",Arial,sans-serif;color:var(--text)}
.deck{display:grid;grid-template-columns:repeat(3,388px);grid-auto-rows:218px;gap:11.25px 8px;padding:10px}
.slide{position:relative;overflow:hidden;background:var(--white)}
.abs{position:absolute}

/* shared pieces */
.footer{position:absolute;left:0;right:0;bottom:0;height:9px;background:var(--bar)}
.footer .url{position:absolute;left:6px;top:0;line-height:9px;font-size:5px;letter-spacing:.3px;color:var(--white)}
.footer .page{position:absolute;right:0;top:0;height:9px;width:44px;background:var(--orange);clip-path:polygon(0 0,100% 0,100% 100%,0 100%,3px 50%);font-size:4.5px;line-height:9px;color:var(--white);text-align:right;padding-right:6px;font-weight:600}
.title{position:absolute;left:8px;top:7px;font-family:"Montserrat",sans-serif;font-weight:600;font-size:13px;color:var(--ink)}
.title::before{content:"";position:absolute;left:-8px;top:1px;width:2px;height:14px;background:var(--bar)}
.title .accent{color:var(--orange)}
.brand{display:flex;align-items:center;gap:4px;font-family:"Montserrat",sans-serif;font-weight:700}
.brand .mark{border-radius:50%;flex:none}
.brand .name{line-height:1}
.brand .name small{display:block;font-size:.3em;letter-spacing:.45em;margin-top:.2em}
.brand-mini{position:absolute;right:6px;top:8px;font-size:9px;color:var(--orange)}
.brand-mini .mark{width:7px;height:7px;background:var(--orange)}
.copy{font-size:5.3px;line-height:8.4px;text-align:justify}
.para-title{font-family:"Montserrat",sans-serif;font-weight:600;font-size:8px;color:var(--orange)}
.dot{position:absolute;width:6px;height:6px;border-radius:50%;background:var(--orange);border:1.2px solid var(--bar)}
.photo{position:absolute}
.cover-title{font-family:"Montserrat",sans-serif;font-weight:700;font-size:16.5px;text-align:right}
.cover-sub{font-size:9px;text-align:right}

/* cover slides */
.s-cover{background:var(--orange)}
.s-cover .glow{left:0;top:0;width:230px;height:218px;background:radial-gradient(ellipse 48% 34% at 28% 50%,rgba(255,255,255,.18),rgba(255,255,255,0) 70%),radial-gradient(ellipse 40% 30% at 72% 50%,rgba(255,255,255,.12),rgba(255,255,255,0) 70%)}
.s-cover .brand,.s-plain .brand{position:absolute;right:10px;top:92px;font-size:26px;color:var(--white)}
.s-cover .brand .mark,.s-plain .brand .mark{width:14px;height:14px;background:var(--white)}
.s-cover .cover-title,.s-plain .cover-title{position:absolute;right:10px;top:137px;color:var(--white)}
.s-cover .cover-sub,.s-plain .cover-sub{position:absolute;right:10px;top:161px;color:var(--white)}
.s-plain{background:linear-gradient(135deg,#e07a0c 0%,#f08a18 45%,#f79a2c 100%)}

/* two-column text */
.s-columns .col{position:absolute;top:58px;width:182px}
.s-columns .col .para-title{margin-left:11px;margin-bottom:2px}
.s-columns .col .dot{left:0;top:1px}

/* white title cover */
.s-light .net{left:0;top:0;width:236px;height:180px;background:radial-gradient(ellipse at 0 0,rgba(247,144,30,.28),rgba(247,144,30,.05) 60%,rgba(255,255,255,0) 75%)}
.s-light .cover-title{position:absolute;right:10px;top:86px;color:var(--orange)}
.s-light .cover-sub{position:absolute;right:10px;top:108px;color:var(--ink)}
.s-light .brand{position:absolute;right:10px;top:152px;font-size:29px;color:var(--orange)}
.s-light .brand .mark{width:15px;height:15px;background:var(--orange)}

/* photo + orange box */
.s-feature .photo{left:0;top:54px;width:160px;height:124px;background:linear-gradient(135deg,#0d2136,#1f4a70 55%,#0c1a2b)}
.s-feature .box{position:absolute;left:162px;top:54px;width:224px;height:124px;background:var(--orange);padding:6px 6px 0 6px;color:var(--white)}
.s-feature .box .para-title{color:var(--white);font-size:8.5px;margin-bottom:5px}
.s-feature .box .copy{font-size:4.8px;line-height:7.2px}
.s-feature .box .copy + .copy{margin-top:5px}

/* stacked bullets */
.s-list .item{position:absolute;left:14px;width:364px}
.s-list .item .dot{left:0;top:1px}
.s-list .item .para-title{font-size:7px;margin-left:12px;margin-bottom:1px}
.s-list .item .copy{margin-left:12px}

/* bullets + photo */
.s-split .para-title{position:absolute;left:14px;top:53px}
.s-split .item{position:absolute;left:16px;width:196px}
.s-split .item .dot{left:0;top:1px}
.s-split .item .copy{margin-left:12px;text-align:left}
.s-split .photo{left:217px;top:35px;width:165px;height:163px;background:linear-gradient(160deg,#8a6f55,#e6e2dc 45%,#c9c4bc 70%,#7a6350)}

/* donut charts */
.s-charts .para-title{position:absolute;left:27px;top:40px;font-size:7px}
.s-charts .intro{position:absolute;left:27px;top:50px;width:352px;text-align:left}
.s-charts .gauge{position:absolute;top:96px;width:86px;text-align:center}
.s-charts .gauge svg{display:block;margin:0 auto}
.s-charts .gauge .label{font-family:"Montserrat",sans-serif;font-weight:600;font-size:7px;margin-top:11px;white-space:nowrap}
.s-charts .gauge .caption{font-size:5.3px;line-height:7.4px;text-align:center;margin-top:2px;white-space:nowrap}

/* process */
.s-process .icon{position:absolute;top:42px;width:24px;height:22px}
.s-process .step{position:absolute;top:74px;width:106px;height:44px}
.s-process .step p{position:absolute;left:22px;right:18px;top:13px;font-size:5px;line-height:6.5px;text-align:center;color:var(--orange)}
.s-process .step.dark p{color:var(--ink)}
.s-process .block{position:absolute;top:140px;width:190px}
.s-process .block .para-title{margin-bottom:2px}

/* two-line heading + photo */
.s-story .heading{position:absolute;left:18px;top:70px;font-family:"Montserrat",sans-serif;font-weight:600;font-size:9px;line-height:12px;color:var(--orange)}
.s-story .copy{position:absolute;left:106px;top:66px;width:100px;font-size:5.2px;line-height:8.1px}
.s-story .photo{left:214px;top:0;width:174px;height:209px;background:linear-gradient(150deg,#3e4a55,#a9a49e 45%,#d8d3ca 65%,#5b4b3d)}

/* team */
.s-team .heading{position:absolute;left:26px;top:88px;font-family:"Montserrat",sans-serif;font-weight:600;font-size:12px;color:var(--orange)}
.s-team .member{position:absolute;top:46px;width:69px;text-align:center}
.s-team .frame{height:80px;background:#d6d6d6}
.s-team .member .para-title{font-size:6px;margin-top:12px}
.s-team .member .copy{text-align:center;font-size:5px;line-height:8.2px;margin:1px -6px 0}

/* triangle chart */
.s-graph .band{position:absolute;left:0;top:38px;width:190px;height:20px;background:var(--orange);color:var(--white);font-family:"Montserrat",sans-serif;font-weight:700;font-size:11px;line-height:20px;text-align:center}
.s-graph .band-dot{position:absolute;left:188px;top:42px;width:13px;height:13px;border-radius:50%;background:var(--bar)}
.s-graph .note{position:absolute;left:206px;top:37px;width:176px;text-align:left}
.s-graph svg{position:absolute;left:0;top:0}

/* image title */
.s-image{background:var(--orange)}
.s-image .photo{left:0;top:0;width:220px;height:209px;background:linear-gradient(140deg,#f4f5f6,#dfe2e5 55%,#c5cad0);clip-path:polygon(0 0,220px 0,172px 209px,0 209px)}
.s-image .brand-mini{color:var(--white)}
.s-image .brand-mini .mark{background:var(--white)}
.big-head{position:absolute;left:224px;top:44px;font-family:"Montserrat",sans-serif;font-weight:700;font-size:18px;line-height:22px;color:var(--white)}
.big-copy{position:absolute;left:224px;top:98px;width:154px;color:var(--white);font-size:5px;line-height:8px}

/* section divider */
.s-divider{background:linear-gradient(135deg,#f08a18,#f7951f)}
.s-divider .brand{position:absolute;left:14px;top:86px;font-size:30px;color:var(--white)}
.s-divider .brand .mark{width:16px;height:16px;background:var(--white)}
.s-divider .rule{position:absolute;left:210px;top:50px;width:1px;height:126px;background:rgba(255,255,255,.85)}
.s-divider .big-head,.s-divider .big-copy{left:222px}

/* closing */
.s-thanks .band{position:absolute;left:0;top:0;width:388px;height:80px;background:var(--orange);color:var(--white);font-family:"Montserrat",sans-serif;font-weight:400;font-size:15px;letter-spacing:.4px;text-align:center;line-height:80px}
.s-thanks .brand{position:absolute;left:46px;top:92px;font-size:18px;color:var(--orange)}
.s-thanks .brand .mark{width:10px;height:10px;background:var(--orange)}
.s-thanks .contact{position:absolute;left:18px;width:180px;display:flex;align-items:center;gap:7px}
.s-thanks .contact svg{flex:none}
.s-thanks .contact .copy{text-align:left}
.s-thanks .map{position:absolute;left:202px;top:84px;width:186px;height:119px;background:linear-gradient(135deg,#e8ede4,#f3f1ea 50%,#dfe7da)}
</style>
</head>
<body>
<main class="deck">

  <!-- 1 cover -->
  <section class="slide s-cover">
    <div class="abs glow" role="img" aria-label="Faint looping network decoration"></div>
    <div class="brand"><span class="mark"></span><span class="name">VELANTIS<small>TECHNOLOGIES</small></span></div>
    <h1 class="cover-title">Project Title Here</h1>
    <p class="cover-sub">Subtext here</p>
  </section>

  <!-- 2 cover alt -->
  <section class="slide s-plain" role="img" aria-label="Orange background with faint network lines">
    <div class="brand"><span class="mark"></span><span class="name">VELANTIS<small>TECHNOLOGIES</small></span></div>
    <h1 class="cover-title">Project Title Here</h1>
    <p class="cover-sub">Subtext here</p>
  </section>

  <!-- 3 two columns -->
  <section class="slide s-columns">
    <h2 class="title"><span class="accent">Project</span> Title here</h2>
    <div class="brand brand-mini"><span class="mark"></span><span class="name">VELANTIS</span></div>
    <div class="col" style="left:8px">
      <span class="dot"></span>
      <h3 class="para-title">Paragraph Title here</h3>
      <p class="copy">Use this space to describe the project in plain words. Explain the goal, the people it serves and the value it brings to the business. Keep each sentence short so the slide stays easy to scan from the back of the room. Add the key numbers that support your message and point to the next steps. Close with a clear line that tells the audience what you want them to remember after the meeting ends. Replace this sample text with your own content before you present.</p>
    </div>
    <div class="col" style="left:198px">
      <span class="dot"></span>
      <h3 class="para-title">Paragraph Title here</h3>
      <p class="copy">Use this space to describe the project in plain words. Explain the goal, the people it serves and the value it brings to the business. Keep each sentence short so the slide stays easy to scan from the back of the room. Add the key numbers that support your message and point to the next steps. Close with a clear line that tells the audience what you want them to remember after the meeting ends. Replace this sample text with your own content before you present.</p>
    </div>
    <footer class="footer"><span class="url">www.velantistech.com</span><span class="page">Page : 01</span></footer>
  </section>

  <!-- 4 light cover -->
  <section class="slide s-light">
    <div class="abs net" role="img" aria-label="Orange network line decoration"></div>
    <h1 class="cover-title">Project Title Here</h1>
    <p class="cover-sub">Subtext here</p>
    <div class="brand"><span class="mark"></span><span class="name">VELANTIS<small>TECHNOLOGIES</small></span></div>
    <footer class="footer"></footer>
  </section>

  <!-- 5 photo + orange box -->
  <section class="slide s-feature">
    <h2 class="title"><span class="accent">Project</span> Title here</h2>
    <div class="brand brand-mini"><span class="mark"></span><span class="name">VELANTIS</span></div>
    <div class="photo" role="img" aria-label="Photo of a person touching a glowing digital network"></div>
    <div class="box">
      <h3 class="para-title">Paragraph Title here</h3>
      <p class="copy">Use this space to describe the project in plain words. Explain the goal, the people it serves and the value it brings to the business. Keep each sentence short so the slide stays easy to scan from the back of the room. Add the key numbers that support your message and point to the next steps. Close with a clear line that tells the audience what you want them to remember after the meeting ends. Replace this sample text with your own content before you present.</p>
      <p class="copy">Add a brief note here that sums up this point in one or two simple lines of text.</p>
    </div>
    <footer class="footer"><span class="url">www.velantistech.com</span><span class="page">Page : 01</span></footer>
  </section>

  <!-- 6 stacked bullets -->
  <section class="slide s-list">
    <h2 class="title"><span class="accent">Project</span> Title here</h2>
    <div class="brand brand-mini"><span class="mark"></span><span class="name">VELANTIS</span></div>
    <div class="item" style="top:46px"><span class="dot"></span><h3 class="para-title">Paragraph Title here</h3><p class="copy">Share one idea in each block so readers can follow along. Give a short reason, one proof point and the result you expect. Keep the tone simple, direct and friendly for every audience you meet.</p></div>
    <div class="item" style="top:91px"><span class="dot"></span><h3 class="para-title">Paragraph Title here</h3><p class="copy">Share one idea in each block so readers can follow along. Give a short reason, one proof point and the result you expect. Keep the tone simple, direct and friendly for every audience you meet.</p></div>
    <div class="item" style="top:136px"><span class="dot"></span><h3 class="para-title">Paragraph Title here</h3><p class="copy">Share one idea in each block so readers can follow along. Give a short reason, one proof point and the result you expect. Keep the tone simple, direct and friendly for every audience you meet.</p></div>
    <footer class="footer"><span class="url">www.velantistech.com</span><span class="page">Page : 01</span></footer>
  </section>

  <!-- 7 bullets + photo -->
  <section class="slide s-split">
    <h2 class="title"><span class="accent">Project</span> Title here</h2>
    <div class="brand brand-mini"><span class="mark"></span><span class="name">VELANTIS</span></div>
    <h3 class="para-title">Paragraph Title here</h3>
    <div class="item" style="top:66px"><span class="dot"></span><p class="copy">Add a brief note here that sums up this point in one or two simple lines of text.</p></div>
    <div class="item" style="top:102px"><span class="dot"></span><p class="copy">Add a brief note here that sums up this point in one or two simple lines of text.</p></div>
    <div class="item" style="top:145px"><span class="dot"></span><p class="copy">Add a brief note here that sums up this point in one or two simple lines of text.</p></div>
    <div class="photo" role="img" aria-label="Top view photo of a desk with a laptop, sketches and coffee"></div>
    <footer class="footer"><span class="url">www.velantistech.com</span><span class="page">Page : 01</span></footer>
  </section>

  <!-- 8 donut charts -->
  <section class="slide s-charts">
    <h2 class="title"><span class="accent">Project</span> Title here</h2>
    <div class="brand brand-mini"><span class="mark"></span><span class="name">VELANTIS</span></div>
    <h3 class="para-title">Paragraph Title here</h3>
    <p class="copy intro">Share one idea in each block so readers can follow along. Give a short reason, one proof point and the result you expect. Keep the tone simple, direct and friendly for every audience you meet.</p>
    <div class="gauge" style="left:12px">
      <svg width="60" height="60" viewBox="0 0 60 60"><circle cx="30" cy="30" r="26" fill="none" stroke="#eeeeee" stroke-width="4"/><circle cx="30" cy="30" r="26" fill="none" stroke="#f7901e" stroke-width="4" pathLength="100" stroke-dasharray="80 100" transform="rotate(-90 30 30)"/><text x="30" y="33.5" text-anchor="middle" font-family="Montserrat, sans-serif" font-size="10" fill="#2b2b2b">80%</text></svg>
      <p class="label" style="color:var(--orange)">Graphics Chart</p>
      <p class="caption">Short caption for this<br>chart goes here</p>
    </div>
    <div class="gauge" style="left:108px">
      <svg width="60" height="60" viewBox="0 0 60 60"><circle cx="30" cy="30" r="26" fill="none" stroke="#eeeeee" stroke-width="4"/><circle cx="30" cy="30" r="26" fill="none" stroke="#b9b9b9" stroke-width="4" pathLength="100" stroke-dasharray="50 100" transform="rotate(-90 30 30)"/><text x="30" y="33.5" text-anchor="middle" font-family="Montserrat, sans-serif" font-size="10" fill="#2b2b2b">50%</text></svg>
      <p class="label" style="color:var(--grey-light)">Graphics Chart</p>
      <p class="caption">Short caption for this<br>chart goes here</p>
    </div>
    <div class="gauge" style="left:195px">
      <svg width="60" height="60" viewBox="0 0 60 60"><circle cx="30" cy="30" r="26" fill="none" stroke="#eeeeee" stroke-width="4"/><circle cx="30" cy="30" r="26" fill="none" stroke="#f9ab55" stroke-width="4" pathLength="100" stroke-dasharray="70 100" transform="rotate(-90 30 30)"/><text x="30" y="33.5" text-anchor="middle" font-family="Montserrat, sans-serif" font-size="10" fill="#2b2b2b">70%</text></svg>
      <p class="label" style="color:var(--orange-soft)">Graphics Chart</p>
      <p class="caption">Short caption for this<br>chart goes here</p>
    </div>
    <div class="gauge" style="left:287px">
      <svg width="60" height="60" viewBox="0 0 60 60"><circle cx="30" cy="30" r="26" fill="none" stroke="#eeeeee" stroke-width="4"/><circle cx="30" cy="30" r="26" fill="none" stroke="#262626" stroke-width="4" pathLength="100" stroke-dasharray="60 100" transform="rotate(-90 30 30)"/><text x="30" y="33.5" text-anchor="middle" font-family="Montserrat, sans-serif" font-size="10" fill="#2b2b2b">60%</text></svg>
      <p class="label" style="color:var(--ink)">Graphics Chart</p>
      <p class="caption">Short caption for this<br>chart goes here</p>
    </div>
    <footer class="footer"><span class="url">www.velantistech.com</span><span class="page">Page : 01</span></footer>
  </section>

  <!-- 9 process -->
  <section class="slide s-process">
    <h2 class="title"><span class="accent">Project</span> Title here</h2>
    <div class="brand brand-mini"><span class="mark"></span><span class="name">VELANTIS</span></div>
    <svg class="icon" style="left:81px" viewBox="0 0 24 22" fill="none" stroke="#f7901e" stroke-width="1.2"><path d="M3 8h4l9-5v16l-9-5H3z"/><path d="M6 14l2 6h3l-2-6"/><path d="M19 8l3-2M19 11h4M19 14l3 2"/></svg>
    <svg class="icon" style="left:178px" viewBox="0 0 24 22" fill="none" stroke="#2b2b2b" stroke-width="1.2"><rect x="2" y="2" width="20" height="13" rx="1"/><path d="M9 19h6M12 15v4"/><path d="M5 6h14M5 9h9" stroke-width=".8"/></svg>
    <svg class="icon" style="left:289px" viewBox="0 0 24 22" fill="none" stroke="#f7901e" stroke-width="1.2"><path d="M2 20h20"/><rect x="4" y="13" width="3" height="7"/><rect x="9" y="10" width="3" height="10"/><rect x="14" y="7" width="3" height="13"/><path d="M4 9l5-3 4 2 7-6M17 2h3v3"/></svg>
    <svg class="step" style="left:37px" viewBox="0 0 106 44"><polygon points="1,1 88,1 105,22 88,43 1,43 17,22" fill="none" stroke="#f7901e" stroke-width="1.2"/></svg>
    <div class="step" style="left:37px"><p>Short note for this step here</p></div>
    <svg class="step" style="left:145px" viewBox="0 0 106 44"><polygon points="1,1 88,1 105,22 88,43 1,43 17,22" fill="none" stroke="#262626" stroke-width="1.2"/></svg>
    <div class="step dark" style="left:145px"><p>Short note for this step here</p></div>
    <svg class="step" style="left:252px" viewBox="0 0 106 44"><polygon points="1,1 88,1 105,22 88,43 1,43 17,22" fill="none" stroke="#f7901e" stroke-width="1.2"/></svg>
    <div class="step" style="left:252px"><p>Short note for this step here</p></div>
    <div class="block" style="left:17px"><h3 class="para-title">Paragraph Title here</h3><p class="copy">Share one idea in each block so readers can follow along. Give a short reason, one proof point and the result you expect. Keep the tone simple, direct and friendly for every audience you meet.</p></div>
    <div class="block" style="left:219px;width:160px"><h3 class="para-title">Paragraph Title here</h3><p class="copy">Share one idea in each block so readers can follow along. Give a short reason, one proof point and the result you expect. Keep the tone simple, direct and friendly for every audience you meet.</p></div>
    <footer class="footer"><span class="url">www.velantistech.com</span><span class="page">Page : 01</span></footer>
  </section>

  <!-- 10 story -->
  <section class="slide s-story">
    <h2 class="title"><span class="accent">Project</span> Title here</h2>
    <h3 class="heading">Two Line<br>Paragraph<br>Text Title here</h3>
    <p class="copy">Use this space to describe the project in plain words. Explain the goal, the people it serves and the value it brings to the business. Keep each sentence short so the slide stays easy to scan from the back of the room. Add the key numbers that support your message and point to the next steps. Close with a clear line that tells the audience what you want them to remember after the meeting ends. Replace this sample text with your own content before you present.</p>
    <div class="photo" role="img" aria-label="Photo of two colleagues talking at a laptop in an office"></div>
    <footer class="footer"><span class="url">www.velantistech.com</span><span class="page">Page : 01</span></footer>
  </section>

  <!-- 11 team -->
  <section class="slide s-team">
    <h2 class="title"><span class="accent">Project</span> Title here</h2>
    <div class="brand brand-mini"><span class="mark"></span><span class="name">VELANTIS</span></div>
    <h3 class="heading">Our Team</h3>
    <div class="member" style="left:113px"><div class="frame"></div><h4 class="para-title">Image text here</h4><p class="copy">Add a brief note here that sums up this point in one or two simple lines of text.</p></div>
    <div class="member" style="left:207px"><div class="frame"></div><h4 class="para-title">Image text here</h4><p class="copy">Add a brief note here that sums up this point in one or two simple lines of text.</p></div>
    <div class="member" style="left:301px"><div class="frame"></div><h4 class="para-title">Image text here</h4><p class="copy">Add a brief note here that sums up this point in one or two simple lines of text.</p></div>
    <footer class="footer"><span class="url">www.velantistech.com</span><span class="page">Page : 01</span></footer>
  </section>

  <!-- 12 graph -->
  <section class="slide s-graph">
    <h2 class="title"><span class="accent">Project</span> Title here</h2>
    <div class="brand brand-mini"><span class="mark"></span><span class="name">VELANTIS</span></div>
    <div class="band">GRAPH TITLE HERE</div>
    <span class="band-dot"></span>
    <p class="copy note">Add a brief note here that sums up this point in one or two simple lines of text.</p>
    <svg width="388" height="218" viewBox="0 0 388 218" font-family="Montserrat, sans-serif">
      <polygon points="58,188 100,116 142,188" fill="#8a8a8a"/>
      <polygon points="94,188 165,88 230,188" fill="#f7901e" opacity=".9"/>
      <polygon points="186,188 230,118 270,188" fill="#cfcfcf" opacity=".9"/>
      <polygon points="242,188 278,128 312,188" fill="#f08a12" opacity=".85"/>
      <text x="101" y="102" text-anchor="middle" font-size="8" fill="#2b2b2b">70%</text>
      <text x="166" y="76" text-anchor="middle" font-size="8" fill="#f7901e">80%</text>
      <text x="231" y="106" text-anchor="middle" font-size="8" fill="#2b2b2b">60%</text>
      <text x="279" y="114" text-anchor="middle" font-size="8" fill="#f7901e">50%</text>
      <g font-family="Open Sans, sans-serif" font-size="5" text-anchor="middle" font-weight="600">
        <text x="93" y="198" fill="#8a8a8a">Graph Text here</text>
        <text x="163" y="198" fill="#f7901e">Graph Text here</text>
        <text x="228" y="198" fill="#bdbdbd">Graph Text here</text>
        <text x="284" y="198" fill="#f7901e">Graph Text here</text>
      </g>
    </svg>
    <footer class="footer"><span class="url">www.velantistech.com</span><span class="page">Page : 01</span></footer>
  </section>

  <!-- 13 image title -->
  <section class="slide s-image">
    <div class="photo" role="img" aria-label="Photo of hands holding a phone over a network diagram sketch"></div>
    <div class="brand brand-mini"><span class="mark"></span><span class="name">VELANTIS</span></div>
    <h2 class="big-head">IMAGE TITLE<br>TEXT HERE</h2>
    <p class="copy big-copy">Share one idea in each block so readers can follow along. Give a short reason, one proof point and the result you expect. Keep the tone simple, direct and friendly for every audience you meet. Add a brief note here that sums up this point in one or two simple lines of text.</p>
    <footer class="footer"><span class="url">www.velantistech.com</span><span class="page">Page : 01</span></footer>
  </section>

  <!-- 14 section divider -->
  <section class="slide s-divider">
    <div class="brand"><span class="mark"></span><span class="name">VELANTIS<small>TECHNOLOGIES</small></span></div>
    <span class="rule"></span>
    <h2 class="big-head">SECTION<br>DIVIDER HERE</h2>
    <p class="copy big-copy">Share one idea in each block so readers can follow along. Give a short reason, one proof point and the result you expect. Keep the tone simple, direct and friendly for every audience you meet. Add a brief note here that sums up this point in one or two simple lines of text.</p>
    <footer class="footer"><span class="url">www.velantistech.com</span><span class="page">Page : 01</span></footer>
  </section>

  <!-- 15 closing -->
  <section class="slide s-thanks">
    <div class="band">THANKS YOU FOR YOUR VALUBLE TIME</div>
    <div class="brand"><span class="mark"></span><span class="name">VELANTIS<small>TECHNOLOGIES</small></span></div>
    <div class="contact" style="top:124px">
      <svg width="18" height="18" viewBox="0 0 18 18" fill="none" stroke="#f7901e" stroke-width=".9"><circle cx="9" cy="9" r="8"/><path d="M5 9l4-3.5L13 9M6 8.3V12.5h6V8.3M8 12.5v-2.5h2v2.5"/></svg>
      <p class="copy">Add your office address or contact line here in short form.</p>
    </div>
    <div class="contact" style="top:151px">
      <svg width="18" height="18" viewBox="0 0 18 18" fill="none" stroke="#f7901e" stroke-width=".9"><circle cx="9" cy="9" r="8"/><path d="M6 4.5h6M6 13.5h6M6.5 4.5c0 3 5 3 5 4.5s-5 1.5-5 4.5M11.5 4.5c0 3-5 3-5 4.5s5 1.5 5 4.5"/></svg>
      <p class="copy">Add your office address or contact line here in short form.</p>
    </div>
    <div class="contact" style="top:177px">
      <svg width="18" height="18" viewBox="0 0 18 18" fill="none" stroke="#f7901e" stroke-width=".9"><circle cx="9" cy="9" r="8"/><rect x="4.5" y="6" width="9" height="6.5"/><path d="M4.5 6l4.5 3.8L13.5 6"/></svg>
      <p class="copy">Add your office address or contact line here in short form.</p>
    </div>
    <div class="map" role="img" aria-label="Street map with a location pin"></div>
    <footer class="footer"><span class="url">www.velantistech.com</span><span class="page">Page : 01</span></footer>
  </section>

</main>
</body>
</html>
```